Birchwood Turf Care_2015 New Cards_V1

We need an enhanced business card from what we have today. We are a Landscaping company and we have an existing Logo and text info that we would like to include.
Text to include:
In business for over 20 years,Fully Insured, Weekly Lawn Maintenance, Spring & Fall Clean-up, Dale Whitford, 203-555-0147, www.birchwoodturfcarect.example, Visit our Website for additional Lawn Care Services or email directly at DALE@BIRCHWOODTURFCARE.EXAMPLE, We appreciate your business.
We want full color background and we will want to take this design and work with a printer that does high graphic silk screen cards. The colors we have thought about are Black, with our Green Logo, with Gold Text...we are open to different colors, we just want the card to wow!

Target Market(s)

Lawn Care Maintenance

Industry/Entity Type

Lawn Care

Contact Information for Business Card

Text to include:
In business for over 20 years, Fully Insured, Weekly Lawn Maintenance, Spring & Fall Clean-up, Dale Whitford, 203-555-0147, www.birchwoodturfcarect.example, Visit our Website for additional Lawn Care Services or email directly at DALE@BIRCHWOODTURFCARE.EXAMPLE, We appreciate your business.

Requirements
Must have
• Logo, text details about how to reach us, standard size business cards that go horizontal.
Nice to have
• background colors, background designs, raised embossed lettering, rounded corners(2 or 4),

```html
<!DOCTYPE html>
<html lang="en">
<head>
<meta charset="utf-8">
<title>Birchwood Turf Care – Business Cards</title>
<link rel="stylesheet" href="https://fonts.googleapis.com/css2?family=Open+Sans:wght@400;600;700&display=swap">
<style>
  :root {
    --backdrop: #5a5a5a;
    --card: #000000;
    --brand-green: #124d15;
    --contact-green: #17531b;
    --grass-light: #1d5a1f;
    --grass-dark: #0a2a0b;
    --gold: #d9a11c;
    --gold-rule: #8a6410;
  }
  * { box-sizing: border-box; margin: 0; padding: 0; }
  html, body { width: 1105px; height: 1200px; overflow: hidden; }
  body {
    background: var(--backdrop);
    font-family: "Open Sans", Arial, sans-serif;
    position: relative;
  }
  .card {
    position: absolute;
    left: 196px;
    width: 720px;
    height: 412px;
    background: var(--card);
    overflow: hidden;
  }
  .card--front { top: 146px; }
  .card--back { top: 602px; }

  .brand {
    display: flex;
    align-items: center;
    gap: 12px;
    color: var(--brand-green);
    font-weight: 700;
    white-space: nowrap;
  }
  .brand__mark {
    border-radius: 50%;
    background: var(--brand-green);
    flex: none;
  }
  .card--front .brand {
    position: absolute;
    left: 47px;
    top: 80px;
    font-size: 30px;
  }
  .card--front .brand__mark { width: 26px; height: 26px; }

  .contact {
    position: absolute;
    left: 44px;
    top: 243px;
    list-style: none;
    color: var(--contact-green);
    font-size: 19px;
    line-height: 28px;
  }
  .contact li { display: flex; align-items: center; gap: 10px; }
  .contact svg { width: 17px; height: 17px; fill: var(--contact-green); flex: none; }

  .holder {
    position: absolute;
    right: 44px;
    top: 272px;
    color: var(--brand-green);
    font-size: 27px;
    font-weight: 700;
  }

  .grass {
    position: absolute;
    left: 0; right: 0; bottom: 0;
    height: 60px;
    background: linear-gradient(to bottom, rgba(29,90,31,0) 0%, var(--grass-light) 55%, var(--grass-dark) 100%);
  }

  .card--back .brand {
    position: absolute;
    left: 0; right: 0;
    top: 92px;
    justify-content: center;
    font-size: 42px;
  }
  .card--back .brand__mark { width: 34px; height: 34px; }

  .details {
    position: absolute;
    left: 0; right: 0;
    top: 232px;
    text-align: center;
    color: var(--gold);
    font-size: 19px;
    line-height: 24.5px;
  }
  .details .rule {
    width: 620px;
    height: 1px;
    margin: 7px auto 6px;
    background: linear-gradient(to right, transparent, var(--gold-rule) 15%, var(--gold-rule) 85%, transparent);
  }
  .details .dot { font-size: 14px; vertical-align: 2px; padding: 0 4px; }
  .details .email { font-weight: 700; }
</style>
</head>
<body>
  <section class="card card--front">
    <div class="brand"><span class="brand__mark"></span>Birchwood Turf Care</div>
    <ul class="contact">
      <li>
        <svg viewBox="0 0 24 24"><path d="M6.6 10.8a15.1 15.1 0 0 0 6.6 6.6l2.2-2.2c.3-.3.7-.4 1-.2 1.1.4 2.3.6 3.6.6.6 0 1 .4 1 1V20c0 .6-.4 1-1 1C10.6 21 3 13.4 3 4c0-.6.4-1 1-1h3.5c.6 0 1 .4 1 1 0 1.3.2 2.5.6 3.6.1.3 0 .7-.2 1z"/></svg>
        203-555-0147
      </li>
      <li>
        <svg viewBox="0 0 24 24"><path d="M2 5h20v14H2z" opacity=".0"/><path d="M2 6l10 7 10-7v12H2z"/><path d="M2 4h20v1.5L12 12 2 5.5z"/></svg>
        info@birchwoodturfcarect.example
      </li>
      <li>
        <svg viewBox="0 0 24 24"><path d="M12 2a10 10 0 1 0 0 20 10 10 0 0 0 0-20zm-1 17.9A8 8 0 0 1 4.1 11H7l2 2v2l2 2zm6.9-2.5c-.3-.8-1-1.4-1.9-1.4h-1v-3c0-.6-.4-1-1-1H8v-2h2c.6 0 1-.4 1-1V7h2c1.1 0 2-.9 2-2v-.4a8 8 0 0 1 2.9 12.8z"/></svg>
        www.birchwoodturfcarect.example
      </li>
    </ul>
    <div class="holder">Dale Whitford</div>
    <div class="grass" role="img" aria-label="Row of green grass blades along the bottom edge"></div>
  </section>

  <section class="card card--back">
    <div class="brand"><span class="brand__mark"></span>Birchwood Turf Care</div>
    <div class="details">
      <p>In business for over 20 years</p>
      <p>Fully Insured <span class="dot">●</span> Weekly Lawn Maintenance <span class="dot">●</span> Spring &amp; Fall Clean-up</p>
      <div class="rule"></div>
      <p>Visit our Website for additional Lawn Care Services or</p>
      <p>email directly at <span class="email">DALE@BIRCHWOODTURFCARE.EXAMPLE</span></p>
      <p>We appreciate your business.</p>
    </div>
  </section>
</body>
</html>
```